Business Card Design Project

Need a business card designed for a horse racing/gambling centered company.
Company name is BrightQuill.com.au
Company colours are similar to those in the logo.
Something clean and modern , designer given liberty to be creative.
Incorporate the logo is preferred.
Single or Double Sided fine
Must include :
Name
Mobile Number
Email Address
Reason: Apologies, I have been traveling unexpectedly with business and just need the extra two days to reply and give feedback before making a decision.
Industry/Entity Type
Business

```html
<!DOCTYPE html>
<html lang="en">
<head>
<meta charset="utf-8">
<title>BrightQuill.com.au business card</title>
<link rel="stylesheet" href="https://fonts.googleapis.com/css2?family=Oswald:wght@400;500&family=Josefin+Sans:wght@400;600&display=swap">
<style>
  :root {
    --page: #d6d8da;
    --dark: #29282c;
    --dark-deep: #1d1c20;
    --paper: #efeeec;
    --paper-shade: #e2e1df;
    --teal: #17958e;
    --teal-light: #3fc1b6;
    --ink: #1b1b1d;
    --emboss: #3a3940;
  }
  * { box-sizing: border-box; margin: 0; padding: 0; }
  html, body { width: 1068px; height: 1200px; overflow: hidden; }
  body {
    background: var(--page);
    position: relative;
    font-family: "Josefin Sans", sans-serif;
  }
  .card {
    position: absolute;
    left: 94px;
    width: 880px;
    height: 503px;
    border-radius: 6px;
    overflow: hidden;
    box-shadow: 0 6px 18px rgba(0,0,0,.22);
  }
  .card--front { top: 60px; background: var(--paper); }
  .card--back {
    top: 637px;
    background: radial-gradient(ellipse at 50% 35%, #3a393e 0%, var(--dark) 45%, var(--dark-deep) 100%);
  }
  .card__shape { position: absolute; inset: 0; }
  .brand-mark {
    position: absolute;
    width: 200px;
    text-align: center;
  }
  .brand-mark__circle {
    width: 170px; height: 170px;
    margin: 0 auto;
    border-radius: 50%;
    background: radial-gradient(circle at 50% 45%, var(--teal-light), var(--teal));
    box-shadow: 0 0 40px rgba(63,193,182,.45);
  }
  .brand-mark__name {
    margin-top: 18px;
    font-family: "Josefin Sans", sans-serif;
    font-weight: 600;
    font-size: 22px;
    color: var(--teal-light);
    white-space: nowrap;
  }
  .card--front .brand-mark { left: 65px; top: 92px; }
  .card--back .brand-mark { left: 340px; top: 92px; }
  .emboss-name {
    position: absolute;
    font-family: "Oswald", sans-serif;
    font-weight: 500;
    font-size: 46px;
    letter-spacing: 1px;
    color: var(--emboss);
    text-shadow: 0 1px 0 rgba(255,255,255,.06), 0 -1px 0 rgba(0,0,0,.5);
  }
  .card--front .emboss-name { left: 30px; top: 380px; }
  .card--back .emboss-name { left: 0; width: 880px; text-align: center; top: 374px; }
  .contact {
    position: absolute;
    left: 426px;
    top: 18px;
    color: var(--ink);
  }
  .contact__name {
    font-family: "Oswald", sans-serif;
    font-weight: 500;
    font-size: 62px;
    line-height: 1;
    color: var(--teal);
    letter-spacing: 1px;
  }
  .contact__role {
    font-family: "Oswald", sans-serif;
    font-size: 18px;
    letter-spacing: 1px;
    margin-top: 2px;
  }
  .contact__address {
    margin-top: 52px;
    font-size: 27px;
    line-height: 50px;
    font-variant: small-caps;
  }
  .contact__online {
    margin-top: 48px;
    font-size: 27px;
    line-height: 40px;
    font-variant: small-caps;
    color: var(--teal);
  }
</style>
</head>
<body>

<section class="card card--front" aria-label="Business card front">
  <svg class="card__shape" viewBox="0 0 880 503" aria-hidden="true">
    <defs>
      <linearGradient id="panelShade" x1="0" y1="0" x2="1" y2="1">
        <stop offset="0" stop-color="#343338"/>
        <stop offset="1" stop-color="#1e1d21"/>
      </linearGradient>
      <linearGradient id="paperShade" x1="0" y1="0" x2="1" y2="1">
        <stop offset="0" stop-color="#f2f1ef"/>
        <stop offset="1" stop-color="#e2e1df"/>
      </linearGradient>
    </defs>
    <rect width="880" height="503" fill="url(#paperShade)"/>
    <polygon points="0,0 402,0 358,200 412,503 0,503" fill="var(--teal)"/>
    <polygon points="0,0 388,0 344,200 398,503 0,503" fill="url(#panelShade)"/>
  </svg>
  <div class="brand-mark">
    <div class="brand-mark__circle"></div>
    <p class="brand-mark__name">BrightQuill.com.au</p>
  </div>
  <p class="emboss-name">BRIGHTQUILL</p>
  <div class="contact">
    <h1 class="contact__name">PETER HARLOW</h1>
    <p class="contact__role">POSITION</p>
    <p class="contact__address">2107 /56 Harbour Lane<br>Sydney, NSW , 2000<br>Phone: 0412555018</p>
    <p class="contact__online">Peter@brightquill.com.au<br>www.brightquill.com.au</p>
  </div>
</section>

<section class="card card--back" aria-label="Business card back">
  <div class="brand-mark">
    <div class="brand-mark__circle"></div>
    <p class="brand-mark__name">BrightQuill.com.au</p>
  </div>
  <p class="emboss-name">BRIGHTQUILL</p>
</section>

</body>
</html>
```